Harbor of Mercy - Team of Rabbis and Doctors Helping Families Dealing with Illness

The Harbor of Mercy is an organization that accompanies families dealing with severe illnesses of a family member. A team of rabbis and doctors provide support and real-time responses to these families.
The site theme is medicine and law, but the target market is religious Jewish families in crisis. Thus, the site design needs to combine:
- professional, conservative, serious
- spiritual
- warm hug

Target Market(s)

religious families suffering a health crisis

Industry/Entity Type

Non-profit organization

Number of Pages Required

1 page

Font styles to use
Sans Serif

Requirements
Must have
• Final design in PSD format. List of fonts used, colors used and link/button colors used in the design.

```html
<!DOCTYPE html>
<html lang="en">
<head>
<meta charset="utf-8">
<title>Harbor of Mercy</title>
<link href="https://fonts.googleapis.com/css2?family=Poppins:wght@300;400;500;600&display=swap" rel="stylesheet">
<style>
:root{
  --orange:#d9850b;
  --navy:#0b0a4a;
  --gray:#f3f3f3;
  --text:#444;
  --white:#fff;
  --line:#d8d8d8;
}
*{box-sizing:border-box;margin:0;padding:0}
html,body{width:1200px;height:5263px;overflow:hidden}
body{font-family:'Poppins',sans-serif;color:var(--text);background:var(--white);position:relative}
.section{position:absolute;left:0;width:1200px}
.abs{position:absolute}
.title{color:var(--orange);font-weight:400;font-size:42px;letter-spacing:.5px}
.center{text-align:center;width:100%}
.btn{display:inline-flex;align-items:center;justify-content:center;background:var(--orange);color:var(--white);font-size:16px}
.arrows{display:flex;gap:16px;justify-content:center}
.arrow{width:36px;height:40px;border:2px solid var(--orange);border-radius:8px;display:flex;align-items:center;justify-content:center;background:var(--white)}
.ph{display:block}

/* top bar */
.topbar{top:0;height:76px;background:var(--orange);color:var(--white);font-size:14px}
.hotline{left:98px;top:16px;width:164px;height:42px;border:2px solid var(--white);display:flex;align-items:center;justify-content:center;font-size:15px}
.contact{top:20px;display:flex;align-items:center;gap:14px}
.icon-circle{width:32px;height:32px;border:2px solid var(--white);border-radius:50%;display:flex;align-items:center;justify-content:center}
.search{left:930px;top:16px;width:184px;height:42px;border:2px solid var(--white);border-radius:22px;display:flex;align-items:center;justify-content:space-between;padding:0 16px 0 26px;font-size:12px}

/* nav */
.nav{top:76px;height:132px;background:var(--navy)}
.brand{left:86px;top:40px;color:var(--orange);font-size:30px;font-weight:600;display:flex;align-items:center;gap:12px}
.brand .mark{width:22px;height:22px;background:var(--orange);border-radius:50%}
.menu{left:536px;top:56px;display:flex;gap:38px;color:var(--white);font-size:16px}
.menu .active{color:var(--orange);border-bottom:2px solid var(--orange);padding-bottom:6px;font-size:18px;margin-top:-3px}
.account{left:976px;top:47px;width:140px;height:42px;border:2px solid var(--orange);color:var(--orange);display:flex;align-items:center;justify-content:center;font-size:15px}

/* hero */
.hero{top:208px;height:869px}
.hero .ph{width:1200px;height:869px;background:linear-gradient(120deg,#7b7774,#b9b3ab 40%,#8b6d58 70%,#5d5550)}
.hero-band{left:0;top:568px;width:1200px;height:301px;background:rgba(20,20,20,.72);text-align:center;color:var(--white)}
.hero-band h1{color:var(--orange);font-weight:400;font-size:56px;margin-top:38px}
.hero-band h2{font-weight:400;font-size:26px;margin-top:10px}
.hero-band p{font-size:15px;line-height:21px;margin:10px auto 0;width:560px}
.hero-band .arrows{margin-top:24px}
.hero-band .arrow{background:transparent;border-color:var(--white)}

/* about */
.about{top:1077px;height:644px}
.video{left:90px;top:111px;width:505px;height:425px;background:linear-gradient(135deg,#c9a07a,#8a5a3a 55%,#3a2418)}
.play{left:222px;top:172px;width:80px;height:80px;border-radius:50%;background:var(--white);opacity:.95;display:flex;align-items:center;justify-content:center}
.about-text{left:625px;top:135px;width:480px}
.about-text p{font-size:15px;line-height:22.5px;margin-top:24px}
.about-text .title{margin-bottom:-4px}
.about-text .btn{width:160px;height:50px;margin-top:40px}

/* moral */
.moral{top:1721px;height:480px;background:var(--gray)}
.moral .title{left:123px;top:68px}
.issues{left:123px;top:162px;list-style:none}
.issues li{display:flex;align-items:center;gap:14px;height:86px;font-size:15px;line-height:21px}
.tick{width:46px;height:46px;border-radius:50%;background:var(--orange);display:flex;align-items:center;justify-content:center;flex:none}
.moral .ph{left:677px;top:53px;width:359px;height:307px;background:linear-gradient(135deg,#d6d3ce,#9d9893 55%,#5e5a57)}
.moral .arrows{left:677px;top:381px;width:359px}

/* services */
.services{top:2201px;height:563px}
.card{top:95px;width:253px;height:386px;background:var(--white);box-shadow:0 2px 8px rgba(0,0,0,.1);text-align:center}
.card .ph{width:253px;height:159px}
.card h3{color:var(--orange);font-weight:500;font-size:17px;margin-top:26px}
.card p{font-size:14px;line-height:20.5px;margin:12px 18px 0}
.card .btn{width:152px;height:36px;margin-top:22px;font-size:15px}

/* testimonials */
.testimonials{top:2764px;height:517px;background:var(--gray)}
.testimonials .title{top:42px}
.tcard{top:139px;width:446px;height:251px;background:var(--white);border-radius:12px;padding:40px 32px 0 36px}
.tcard .head{display:flex;align-items:center;gap:18px}
.avatar{width:86px;height:86px;border-radius:50%;background:linear-gradient(135deg,#c27a4a,#6b3a22)}
.stars{color:var(--orange);font-size:17px;letter-spacing:1px}
.tcard .name{font-size:18px;color:#333}
.tcard .role{font-size:16px;color:var(--orange);font-style:italic}
.tcard p{font-size:13.5px;line-height:20.5px;margin-top:16px}
.testimonials .arrows{top:437px}

/* news */
.news{top:3281px;height:678px}
.news .title{top:78px}
.ncard{top:149px;width:323px;height:400px;border:1px solid #e2e2e2;padding:10px}
.ncard .ph{width:303px;height:200px}
.ncard .date{font-size:15px;margin:20px 0 0 16px;color:#333}
.ncard h4{color:var(--orange);font-weight:400;font-size:16px;margin:12px 0 0 16px}
.ncard p{font-size:14.5px;line-height:22px;margin:12px 16px 0 16px}
.ncard .more{color:var(--orange);font-size:13px;margin:10px 0 0 18px;display:flex;align-items:center;gap:8px}
.news .arrows{top:609px}

/* ask */
.ask{top:3959px;height:709px;background:var(--gray)}
.ask .title{top:76px}
.field{left:184px;width:834px;border:1px solid var(--line);background:var(--white);font-size:16px;color:#888;padding:17px 20px}
.send{left:495px;top:517px;width:212px;height:56px;border:1.5px solid var(--orange);color:var(--orange);font-size:20px;display:flex;align-items:center;justify-content:center}

/* footer */
.footer{top:4668px;height:497px;background:var(--navy);color:var(--white)}
.newsletter{left:125px;top:-89px;width:950px;height:171px;background:var(--orange);color:var(--white);border-radius:4px}
.newsletter h3{position:absolute;left:60px;top:30px;font-weight:400;font-size:30px}
.newsletter p{position:absolute;left:60px;top:88px;font-size:14px;line-height:18px;width:330px}
.subscribe{position:absolute;left:518px;top:52px;width:374px;height:58px;background:var(--white);border-radius:30px;display:flex;align-items:center;justify-content:space-between;padding:0 6px 0 24px;color:#888;font-size:14px}
.subscribe span.btn{width:120px;height:44px;border-radius:24px;font-size:15px}
.foot-brand{left:112px;top:262px;color:var(--orange);font-size:40px;font-weight:600;display:flex;align-items:center;gap:14px}
.foot-brand .mark{width:28px;height:28px;background:var(--orange);border-radius:50%}
.foot-col h5{color:var(--orange);font-weight:500;font-size:20px}
.foot-col .rule{width:42px;height:3px;background:var(--orange);margin-top:8px}
.links{list-style:none;margin-top:32px}
.links li{font-size:15px;height:31px;display:flex;align-items:center;gap:14px}
.links li::before{content:"›";color:var(--orange);font-size:20px}
.contacts{margin-top:36px}
.contacts .row{display:flex;gap:22px;align-items:center;height:62px;font-size:14.5px;line-height:17px}
.sq{width:30px;height:30px;border:1.5px solid var(--orange);border-radius:5px;display:flex;align-items:center;justify-content:center;flex:none}
.bottombar{top:5165px;height:98px;background:var(--orange);color:var(--white)}
.social{left:90px;top:28px;display:flex;gap:10px}
.social span{width:42px;height:42px;border:2px solid var(--white);border-radius:50%;display:flex;align-items:center;justify-content:center}
.social span i{width:14px;height:14px;background:var(--white);border-radius:50%}
.copy{right:90px;top:38px;font-size:14.5px}
</style>
</head>
<body>

<header class="section topbar">
  <div class="abs hotline">24/7 Hotline</div>
  <div class="abs contact" style="left:532px">
    <span class="icon-circle"><svg width="14" height="14" viewBox="0 0 24 24"><path d="M6.6 10.8c1.4 2.8 3.8 5.1 6.6 6.6l2.2-2.2c.3-.3.7-.4 1-.2 1.1.4 2.3.6 3.6.6.6 0 1 .4 1 1V20c0 .6-.4 1-1 1C10.6 21 3 13.4 3 4c0-.6.4-1 1-1h3.5c.6 0 1 .4 1 1 0 1.3.2 2.5.6 3.6.1.3 0 .7-.2 1L6.6 10.8z" fill="#fff"/></svg></span>
    <span>5550102030</span>
  </div>
  <div class="abs contact" style="left:724px">
    <span class="icon-circle"><svg width="10" height="10"><circle cx="5" cy="5" r="4" fill="#fff"/></svg></span>
    <span>United Emirates</span>
  </div>
  <div class="abs search"><span>Search</span>
    <svg width="16" height="16" viewBox="0 0 16 16"><circle cx="6.5" cy="6.5" r="5" stroke="#fff" stroke-width="1.6" fill="none"/><path d="M10.5 10.5L15 15" stroke="#fff" stroke-width="1.6"/></svg>
  </div>
</header>

<nav class="section nav">
  <div class="abs brand"><span class="mark"></span>Harbor of Mercy</div>
  <div class="abs menu">
    <span class="active">Home</span><span>Courses</span><span>Conferences</span><span>Leactures</span>
  </div>
  <div class="abs account">My Account</div>
</nav>

<section class="section hero">
  <div class="ph" role="img" aria-label="Doctor in a white coat beside a smiling mother hugging her daughter"></div>
  <div class="abs hero-band">
    <h1>Quality Health Care For Family</h1>
    <h2>Should morphine be given to the patient?</h2>
    <p>Lorem ipsum dolor sit amet, consectetur adipiscing elit, sed do eiusmod tempor incididunt ut labore et dolore magna aliqua.</p>
    <div class="arrows">
      <span class="arrow"><svg width="10" height="14"><path d="M8 1L2 7l6 6" stroke="#fff" stroke-width="2" fill="none"/></svg></span>
      <span class="arrow"><svg width="10" height="14"><path d="M2 1l6 6-6 6" stroke="#fff" stroke-width="2" fill="none"/></svg></span>
    </div>
  </div>
</section>

<section class="section about">
  <div class="abs video" role="img" aria-label="Two pairs of hands clasped together in support">
    <div class="abs play"><svg width="36" height="40"><path d="M4 2l30 18-30 18z" fill="#111"/></svg></div>
  </div>
  <div class="abs about-text">
    <h2 class="title">About Us</h2>
    <p>The Harbor of Mercy is an organization that accompanies families dealing with severe illnesses of a family member. A team of rabbis and doctors provide support and real-time accumsan lacus vel facilisis.</p>
    <p>Thefamilies dealing with severe illnesses of a family member as team of rabbis and doctors provide support and real-time responses to these families.</p>
    <span class="btn">Read More</span>
  </div>
</section>

<section class="section moral">
  <h2 class="abs title">Moral Issues</h2>
  <ul class="abs issues">
    <li><span class="tick"><svg width="22" height="18"><path d="M2 9l6 6L20 3" stroke="#fff" stroke-width="3" fill="none"/></svg></span>The Harbor of Mercy is an organization dealing<br>illnesses of a family &nbsp;member</li>
    <li><span class="tick"><svg width="22" height="18"><path d="M2 9l6 6L20 3" stroke="#fff" stroke-width="3" fill="none"/></svg></span>The Harbor of Mercy is an organization dealing<br>illnesses of a family &nbsp;member</li>
    <li><span class="tick"><svg width="22" height="18"><path d="M2 9l6 6L20 3" stroke="#fff" stroke-width="3" fill="none"/></svg></span>The Harbor of Mercy is an organization dealing<br>illnesses of a family &nbsp;member</li>
  </ul>
  <div class="abs ph" role="img" aria-label="Woman in a headscarf praying with folded hands beside a bed"></div>
  <div class="abs arrows">
    <span class="arrow"><svg width="10" height="14"><path d="M8 1L2 7l6 6" stroke="#d9850b" stroke-width="2" fill="none"/></svg></span>
    <span class="arrow"><svg width="10" height="14"><path d="M2 1l6 6-6 6" stroke="#d9850b" stroke-width="2" fill="none"/></svg></span>
  </div>
</section>

<section class="section services">
  <div class="abs card" style="left:76px">
    <div class="ph" role="img" aria-label="Woman recording a course at a desk with a computer" style="background:linear-gradient(135deg,#e4e1dc,#a49a8f)"></div>
    <h3>COURSES</h3>
    <p>Lincididunt ut labore et dolore magna aliqua. &nbsp;accumsan lacus vel facilisis.</p>
    <span class="btn">Read More</span>
  </div>
  <div class="abs card" style="left:341px">
    <div class="ph" role="img" aria-label="Group of women discussing at a conference table" style="background:linear-gradient(135deg,#a88a6e,#5a3d2c)"></div>
    <h3>CONFERENCES</h3>
    <p>Lincididunt ut labore et dolore magna aliqua. &nbsp;accumsan lacus vel facilisis.</p>
    <span class="btn">Read More</span>
  </div>
  <div class="abs card" style="left:607px">
    <div class="ph" role="img" aria-label="Lecturer talking with a student in front of a chalkboard" style="background:linear-gradient(135deg,#4d5a4e,#262a26)"></div>
    <h3>LECTURES</h3>
    <p>Lincididunt ut labore et dolore magna aliqua. &nbsp;accumsan lacus vel facilisis.</p>
    <span class="btn">Read More</span>
  </div>
  <div class="abs card" style="left:873px">
    <div class="ph" role="img" aria-label="Woman at a desk answering the hotline beside a computer" style="background:linear-gradient(135deg,#e4e1dc,#a49a8f)"></div>
    <h3>HOTLINE 24/7</h3>
    <p>Lincididunt ut labore et dolore magna aliqua. &nbsp;accumsan lacus vel facilisis.</p>
    <span class="btn">Read More</span>
  </div>
</section>

<section class="section testimonials">
  <h2 class="abs title center">What The Client Says</h2>
  <div class="abs tcard" style="left:155px">
    <div class="head">
      <div class="avatar" role="img" aria-label="Client portrait"></div>
      <div><div class="stars">★★★★★</div><div class="name">Dana Morel</div><div class="role">Organiser</div></div>
    </div>
    <p>Lorem ipsum dolor sit amet, consectetur adipiscing elit, sed do eiusmod tempor incididunt ut labore et dolore lacus vel facilisis.</p>
  </div>
  <div class="abs tcard" style="left:619px;padding-left:40px">
    <div class="head">
      <div class="avatar" role="img" aria-label="Client portrait" style="background:linear-gradient(135deg,#8a8a8a,#d1a12a)"></div>
      <div><div class="stars">★★★★★</div><div class="name">Elias Brook</div><div class="role">Organiser</div></div>
    </div>
    <p>Lorem ipsum dolor sit amet, consectetur adipiscing elit, sed do eiusmod tempor incididunt ut labore et dolore lacus vel facilisis.</p>
  </div>
  <div class="abs arrows" style="width:1200px">
    <span class="arrow"><svg width="10" height="14"><path d="M8 1L2 7l6 6" stroke="#d9850b" stroke-width="2" fill="none"/></svg></span>
    <span class="arrow"><svg width="10" height="14"><path d="M2 1l6 6-6 6" stroke="#d9850b" stroke-width="2" fill="none"/></svg></span>
  </div>
</section>

<section class="section news">
  <h2 class="abs title center">Our Latest News</h2>
  <div class="abs ncard" style="left:98px">
    <div class="ph" role="img" aria-label="Audience seated in a seminar room facing a presentation" style="background:linear-gradient(135deg,#d8d8d8,#6f6f6f)"></div>
    <div class="date">Monday 21 ,12,2024</div>
    <h4>RAISE BRAND AWARENESS</h4>
    <p>If you've suffered an injury due to the negligence of a company, .</p>
  </div>
  <div class="abs ncard" style="left:435px">
    <div class="ph" role="img" aria-label="Teacher recording a lesson at a whiteboard" style="background:linear-gradient(135deg,#cfd3d6,#4f5560)"></div>
    <div class="date">Monday 21 ,12,2024</div>
    <h4>RAISE BRAND AWARENESS</h4>
    <p>Construction careers involve some of the most conditions.</p>
    <div class="more">READ MORE <svg width="16" height="16"><circle cx="8" cy="8" r="7" stroke="#d9850b" stroke-width="1.4" fill="none"/><path d="M7 5l3 3-3 3" stroke="#d9850b" stroke-width="1.4" fill="none"/></svg></div>
  </div>
  <div class="abs ncard" style="left:773px">
    <div class="ph" role="img" aria-label="Students in a lecture hall" style="background:linear-gradient(135deg,#c8923c,#6e4b2a)"></div>
    <div class="date">Monday 21 ,12,2024</div>
    <h4>RAISE BRAND AWARENESS</h4>
    <p>Services have reinvented modern travel at our very fingertips.</p>
  </div>
  <div class="abs arrows" style="width:1200px">
    <span class="arrow"><svg width="10" height="14"><path d="M8 1L2 7l6 6" stroke="#d9850b" stroke-width="2" fill="none"/></svg></span>
    <span class="arrow"><svg width="10" height="14"><path d="M2 1l6 6-6 6" stroke="#d9850b" stroke-width="2" fill="none"/></svg></span>
  </div>
</section>

<section class="section ask">
  <h2 class="abs title center">Ask The Rabbi</h2>
  <div class="abs field" style="top:150px;height:56px">Full Name</div>
  <div class="abs field" style="top:215px;height:56px">E Mail Addrees</div>
  <div class="abs field" style="top:278px;height:56px">Phone Number</div>
  <div class="abs field" style="top:344px;height:141px;padding-top:22px">Full Name</div>
  <div class="abs send">Send Message</div>
</section>

<footer class="section footer">
  <div class="abs newsletter">
    <h3>Newsletter Sign Up!</h3>
    <p>Lorem ipsum dolor sit amet, consectetur adipiscing elit, sed do eiusmod tempor</p>
    <div class="subscribe">Email here <span class="btn">SUMBIT</span></div>
  </div>
  <div class="abs foot-brand"><span class="mark"></span>Harbor of Mercy</div>
  <div class="abs foot-col" style="left:517px;top:188px">
    <h5>Quick Links</h5><div class="rule"></div>
    <ul class="links"><li>Home</li><li>About Us</li><li>Our Services</li><li>Our Blogs</li><li>Testimonials</li></ul>
  </div>
  <div class="abs foot-col" style="left:775px;top:186px">
    <h5>Our Newsletter</h5><div class="rule"></div>
    <div class="contacts">
      <div class="row"><span class="sq"><svg width="12" height="12" viewBox="0 0 24 24"><path d="M6.6 10.8c1.4 2.8 3.8 5.1 6.6 6.6l2.2-2.2c.3-.3.7-.4 1-.2 1.1.4 2.3.6 3.6.6.6 0 1 .4 1 1V20c0 .6-.4 1-1 1C10.6 21 3 13.4 3 4c0-.6.4-1 1-1h3.5c.6 0 1 .4 1 1 0 1.3.2 2.5.6 3.6.1.3 0 .7-.2 1L6.6 10.8z" fill="#d9850b"/></svg></span><span>CALL US<br>(555) 014-2290</span></div>
      <div class="row"><span class="sq"><svg width="14" height="10"><rect x="1" y="1" width="12" height="8" stroke="#d9850b" fill="none"/><path d="M1 1l6 5 6-5" stroke="#d9850b" fill="none"/></svg></span><span>EMAIL US<br>hello@harborofmercy.org</span></div>
      <div class="row"><span class="sq"><svg width="12" height="14"><path d="M6 13C2 8 1 6.5 1 5a5 5 0 0110 0c0 1.5-1 3-5 8z" fill="#d9850b"/><circle cx="6" cy="5" r="1.8" fill="#0b0a4a"/></svg></span><span>The dummy adress Is here<br>&amp;the Location</span></div>
    </div>
  </div>
</footer>

<div class="section bottombar">
  <div class="abs social"><span><i></i></span><span><i></i></span><span><i></i></span><span><i></i></span></div>
  <div class="abs copy">All Rights Reserved @ Copyrights 2023</div>
</div>

</body>
</html>
```